手延うどん(乾麺)のパッケージデザイン(製品袋)を依頼させて頂きます。和紙系か和紙雲竜系の袋を考えていますので高級感のあるデザインを希望します。ターゲット層は40-60代の価格ではなく美味しさを求めているお客様。何本か並べると綺麗なデザイン。※現在販売しているデザインだと、シンプルすぎるかなと感じています。
サイズ:W50×D27×H25mm
参考に現在のデザイン写真を添付しておきます。
サイズが間違っていました。横50mm、縦270mm、厚み25mmです。
新たな写真を添付致しました。

和のイメージと背景の小麦のデザイン。温故知新も決め手のポイントでした。

今回、たくさんのデザイン案ありがとうございました。ミトリエさんを通してお願いしたのが初めてで、選ぶのに苦労しました・・・。次回もお願いしようと考えているので、機会がございましたら、またよろしくお願い致します。

```html
<!DOCTYPE html>
<html lang="ja">
<head>
<meta charset="utf-8">
<title>上州 手延うどん パッケージ</title>
<link rel="stylesheet" href="https://fonts.googleapis.com/css2?family=Zen+Antique&display=swap">
<style>
  :root {
    --bg: #ffffff;
    --paper-light: #f1ece3;
    --paper-dark: #e3dacd;
    --stripe: #fbf9f5;
    --ink-brown: #8a6a2c;
    --seal-red: #b0301f;
  }
  html, body {
    margin: 0;
    padding: 0;
    width: 848px;
    height: 1200px;
    overflow: hidden;
    background: var(--bg);
  }
  .canvas {
    position: relative;
    width: 848px;
    height: 1200px;
  }
  .brand-font {
    font-family: "Zen Antique", "Noto Serif JP", serif;
  }
  .package {
    position: absolute;
    display: block;
    box-shadow: 0 1px 3px rgba(0, 0, 0, 0.12);
  }
  .package--large {
    left: 466px;
    top: 62px;
    width: 198px;
    height: 1063px;
  }
  .package-row {
    position: absolute;
    left: 99px;
    top: 656px;
    display: flex;
    gap: 4px;
  }
  .package--small {
    position: static;
    width: 104px;
    height: 475px;
  }
  .label-region { fill: var(--ink-brown); }
  .label-name { fill: var(--ink-brown); writing-mode: vertical-rl; }
  .seal { fill: var(--seal-red); }
  .stripe { fill: var(--stripe); }
  .band { fill: var(--ink-brown); }
</style>
</head>
<body>
<main class="canvas">
  <svg width="0" height="0" style="position:absolute" aria-hidden="true">
    <defs>
      <linearGradient id="paper" x1="0" y1="0" x2="1" y2="1">
        <stop offset="0" stop-color="var(--paper-light)"/>
        <stop offset="0.5" stop-color="var(--paper-dark)"/>
        <stop offset="1" stop-color="var(--paper-light)"/>
      </linearGradient>

      <symbol id="pack-large" viewBox="0 0 200 1064">
        <rect width="200" height="1064" fill="url(#paper)" role="img" aria-label="和紙雲竜柄の地"/>
        <rect class="stripe" x="132" y="0" width="3" height="1064"/>
        <rect class="stripe" x="141" y="0" width="3" height="1064"/>
        <rect class="stripe" x="150" y="0" width="3" height="1064"/>
        <rect class="stripe" x="159" y="0" width="3" height="1064"/>
        <rect class="stripe" x="168" y="0" width="3" height="1064"/>
        <text class="label-region brand-font" x="28" y="96" font-size="36">上州</text>
        <rect class="band" x="0" y="118" width="200" height="9"/>
        <rect class="band" x="0" y="142" width="200" height="9"/>
        <text class="label-name brand-font" x="78" y="195" font-size="80" letter-spacing="16">手延うどん</text>
        <rect class="seal" x="52" y="890" width="50" height="54" role="img" aria-label="朱色の落款"/>
      </symbol>

      <symbol id="pack-small" viewBox="0 0 104 475">
        <rect width="104" height="475" fill="url(#paper)" role="img" aria-label="和紙雲竜柄の地"/>
        <rect class="stripe" x="68" y="0" width="2" height="475"/>
        <rect class="stripe" x="74" y="0" width="2" height="475"/>
        <rect class="stripe" x="80" y="0" width="2" height="475"/>
        <rect class="stripe" x="86" y="0" width="2" height="475"/>
        <rect class="stripe" x="92" y="0" width="2" height="475"/>
        <text class="label-region brand-font" x="16" y="76" font-size="22">上州</text>
        <rect class="band" x="0" y="96" width="104" height="5"/>
        <rect class="band" x="0" y="109" width="104" height="5"/>
        <text class="label-name brand-font" x="42" y="142" font-size="42" letter-spacing="5">手延うどん</text>
        <rect class="seal" x="28" y="400" width="28" height="30" role="img" aria-label="朱色の落款"/>
      </symbol>
    </defs>
  </svg>

  <section class="package-row" aria-label="三本並べた状態">
    <svg class="package package--small" viewBox="0 0 104 475"><use href="#pack-small"/></svg>
    <svg class="package package--small" viewBox="0 0 104 475"><use href="#pack-small"/></svg>
    <svg class="package package--small" viewBox="0 0 104 475"><use href="#pack-small"/></svg>
  </section>

  <svg class="package package--large" viewBox="0 0 200 1064" aria-label="上州 手延うどん 製品袋"><use href="#pack-large"/></svg>
</main>
</body>
</html>
```